Label Redesign For Hemp Oil Tincture Bottle*

I need a label redesigned for Marbleleaf Hemp, current bottle label and logo is attached. The current label doesn't standout, not sure if its the font size or colors on the existing label. It is very important to have on the label that this is a Premium Full Spectrum Hemp Oil that is 2000mg. Then after the label is redesigned and approved, I would need to packaging to be designed to match the approved label design.
This Hemp oil has a relaxing effect to help ease mental and emotional stress, tension and worry. The Omega Fatty Acids it contains also naturally improves your mood and overall brain function, causing you to feel more alert and focused. Hemp Oil helps with insomnia. Take some 2-3 hours before bedtime, you will feel relaxed yet aware of how tired you are that it will lead to a good night's sleep. Hemp Oil helps ease chronic pain and inflammation from conditions such as arthritis, fibromyalgia, lupus, and MS. As a pain relief supplement, it is a safer, natural, non-chemical and non-addictive alternative to prescription painkillers.

Target Market(s)

Adults

Industry/Entity Type

Supplement

Font styles to use
Serif
Sans Serif

Colors

Designer to choose colors to be used in the design.

Requirements
Must have
• All information thats on current label but where it says 750 in the front of the existing label, it needs to say 2000. The 2000 should be prominent on the label.

```html
<!DOCTYPE html>
<html lang="en">
<head>
<meta charset="UTF-8">
<title>Marbleleaf Hemp – Premium Full Spectrum Hemp Oil Label</title>
<link href="https://fonts.googleapis.com/css2?family=Cormorant+Garamond:wght@500;600;700&display=swap" rel="stylesheet">
<style>
  :root {
    --page-bg: #f4f4f4;
    --label-bg: #2e2f33;
    --label-edge: #26272a;
    --leaf-tone: rgba(120, 120, 124, 0.28);
    --accent-green: #bcd38e;
    --title-grey: #c4c4c6;
    --fine-grey: #a6a6a8;
    --mark-dot: #9fbf6a;
  }
  * { margin: 0; padding: 0; box-sizing: border-box; }
  html, body {
    width: 1200px;
    height: 1000px;
    overflow: hidden;
    background: var(--page-bg);
  }
  .canvas {
    width: 1200px;
    height: 1000px;
    display: flex;
    align-items: center;
    justify-content: center;
  }
  .label {
    position: relative;
    width: 860px;
    height: 940px;
    background: linear-gradient(180deg, var(--label-bg) 0%, var(--label-edge) 100%);
    overflow: hidden;
    font-family: "Cormorant Garamond", Georgia, serif;
    text-align: center;
  }
  .leaf-decor {
    position: absolute;
    border-radius: 50%;
    background: radial-gradient(circle, var(--leaf-tone) 0%, rgba(120,120,124,0.12) 55%, rgba(120,120,124,0) 72%);
  }
  .leaf-decor--upper { width: 520px; height: 520px; left: -150px; top: -40px; }
  .leaf-decor--lower { width: 460px; height: 460px; right: -110px; bottom: 40px; }
  .label-content {
    position: relative;
    z-index: 1;
    display: flex;
    flex-direction: column;
    align-items: center;
    padding-top: 90px;
  }
  .brand-mark {
    width: 92px;
    height: 92px;
    border-radius: 50%;
    background: var(--mark-dot);
    margin-bottom: 26px;
  }
  .brand-name {
    color: var(--accent-green);
    font-weight: 600;
    font-size: 48px;
    letter-spacing: 0.5px;
    margin-bottom: 70px;
  }
  .product-title {
    color: var(--title-grey);
    font-weight: 500;
    font-size: 92px;
    line-height: 0.92;
    margin-bottom: 34px;
  }
  .strength {
    color: var(--accent-green);
    font-weight: 600;
    font-size: 64px;
    letter-spacing: 1px;
    margin-bottom: 100px;
  }
  .fine-print {
    color: var(--fine-grey);
    font-weight: 500;
    font-size: 30px;
    line-height: 1.1;
    letter-spacing: 0.5px;
  }
  .flavor {
    color: var(--accent-green);
    font-weight: 700;
    font-size: 30px;
    margin-top: 8px;
  }
</style>
</head>
<body>
  <main class="canvas">
    <section class="label">
      <div class="leaf-decor leaf-decor--upper" role="img" aria-label="Faint hemp leaf decoration"></div>
      <div class="leaf-decor leaf-decor--lower" role="img" aria-label="Faint hemp leaf decoration"></div>
      <div class="label-content">
        <span class="brand-mark" aria-hidden="true"></span>
        <p class="brand-name">Marbleleaf Hemp</p>
        <h1 class="product-title">Premium Full<br>Spectrum<br>Hemp Oil</h1>
        <p class="strength">2000 MG</p>
        <p class="fine-print">DIETARY SUPPLEMENT<br>1FL.OZ(30ML)</p>
        <p class="flavor">Natural Peppermint Flavor</p>
      </div>
    </section>
  </main>
</body>
</html>
```